Marketing Thornbury

We are a primary school and would like to market our school in a positive light. We have had recent success and would like the local community to know!

Target Market(s)

Parents/Carers in the local community

Industry/Entity Type

School

Font styles to use
Serif

Requirements
Must have
• Thornbury Logo first with our moto 'Opening Minds Side by Side'

Reference to the fact we are converting to academy status on 1st April 2014 with The Harrowby BRIDGE Academy Trust

Reference to the partnership with Caldwick Primary School which has bought recent, quick success

Reference to Edvisor rating of Good. Feb 2014
Nice to have
• School colours dark red

Link to website www.thornburyprimary.example

Link to the academy website www.harrowbybridge.example

Statements from Edvisor -

'This is a good school'

'The Executive Headteacher and leadership team have skilfully steered the school's recovery and galvanised staff at all levels to work as a team'

'This is a very different school to the one that existed at the time of the previous inspection'

'Pupils achievement has improved very quickly this year'

'Pupils make a strong start in the school'

'The quality of teaching is good'

'The behaviour of pupils is good'

```html
<!DOCTYPE html>
<html lang="en">
<head>
<meta charset="utf-8">
<title>Thornbury School – Opening Minds Side by Side</title>
<link rel="stylesheet" href="https://fonts.googleapis.com/css2?family=Lato:wght@400;700;900&display=swap">
<style>
  :root {
    --maroon: #5a1220;
    --maroon-bright: #7c1528;
    --slate: #3b4551;
    --body-text: #6c6888;
    --ink: #1c1c22;
    --page: #ffffff;
    --backdrop: #ebe5ee;
    --green: #5d8a4e;
  }
  * { box-sizing: border-box; margin: 0; padding: 0; }
  html, body {
    width: 1200px; height: 750px; overflow: hidden;
    background: var(--backdrop);
    font-family: "Lato", Arial, sans-serif;
  }
  .flyer {
    position: absolute; left: 356px; top: 35px;
    width: 488px; height: 680px;
    background: var(--page);
    box-shadow: 0 14px 30px rgba(60, 30, 70, 0.25);
  }
  .flyer > * { position: absolute; }

  .hero-photo {
    left: 16px; top: 14px; width: 302px; height: 203px;
    border-bottom-right-radius: 42px;
    background: linear-gradient(160deg, #7fb2e4 0%, #e9a24a 40%, #d8463c 65%, #e9d27a 100%);
  }
  .school-name {
    left: 343px; top: 60px; width: 124px;
    display: flex; align-items: center; gap: 8px;
    color: var(--maroon); font-weight: 900; font-size: 16px;
    line-height: 1.15; text-transform: uppercase;
  }
  .school-name .mark {
    flex: none; width: 14px; height: 14px; background: var(--maroon);
  }
  .motto {
    left: 0; top: 236px; width: 100%;
    text-align: center; font-size: 32px; font-weight: 700;
    color: var(--slate); letter-spacing: -0.3px;
  }
  .motto .lead { color: var(--maroon-bright); }

  .feature {
    border-left: 5px solid var(--maroon);
    padding-left: 37px;
  }
  .feature h2 {
    font-size: 15px; font-weight: 700; color: var(--ink); margin-bottom: 5px;
  }
  .feature h2 .accent { color: var(--maroon-bright); }
  .feature p {
    font-size: 10px; line-height: 1.3; color: var(--body-text); margin-bottom: 4px;
  }
  .feature--good { left: 8px; top: 290px; width: 230px; }
  .feature--beyond { left: 252px; top: 290px; width: 228px; }
  .feature--schedule { left: 8px; top: 380px; width: 225px; }

  .class-photo { top: 382px; width: 114px; height: 90px; }
  .class-photo--room { left: 237px; background: linear-gradient(140deg, #c9cfd8, #8c93a3 60%, #d8c2a8); }
  .class-photo--board { left: 359px; border-bottom-right-radius: 24px; background: linear-gradient(140deg, #5e6866, #8b918d 55%, #c9c3ba); }

  .pupils-photo {
    left: 16px; top: 491px; width: 258px; height: 121px;
    background: linear-gradient(90deg, #f2f2f4, #cfd8e6 30%, #e8d6d2 60%, #f2f2f4);
  }
  .why-box {
    left: 275px; top: 490px; width: 199px; height: 122px;
    background: var(--maroon); color: #fff;
    border-top-left-radius: 26px; border-bottom-right-radius: 26px;
    padding: 10px 14px 0 18px;
  }
  .why-box h2 { font-size: 20px; font-weight: 700; margin-bottom: 7px; }
  .why-box p { font-size: 10px; line-height: 1.3; color: #f0e4e6; margin-bottom: 4px; }

  .web-links {
    left: 16px; top: 634px; font-size: 14px; font-weight: 900;
    color: var(--ink); line-height: 1.3; text-transform: uppercase;
  }
  .trust-name {
    left: 300px; top: 628px; width: 176px;
    display: flex; align-items: center; gap: 8px;
    color: var(--green); font-size: 15px; font-weight: 400;
    line-height: 1.1; text-transform: uppercase;
  }
  .trust-name .mark {
    flex: none; width: 16px; height: 16px; border-radius: 50%; background: var(--green);
  }
</style>
</head>
<body>
  <main class="flyer">
    <div class="hero-photo" role="img" aria-label="Photo of smiling pupils huddled together under a blue sky"></div>

    <div class="school-name"><span class="mark"></span><span>Thornbury School</span></div>

    <h1 class="motto"><span class="lead">Opening</span> Minds Side by Side</h1>

    <section class="feature feature--good">
      <h2><span class="accent">Good</span> School</h2>
      <p>Rated Good by Edvisor, Feb 2014: “The quality of teaching is good. The behaviour of pupils is good.”</p>
    </section>

    <section class="feature feature--beyond">
      <h2><span class="accent">Beyond</span> Classroom</h2>
      <p>Our partnership with Caldwick Primary School has brought recent, quick success for every pupil.</p>
    </section>

    <section class="feature feature--schedule">
      <h2><span class="accent">Better</span> Schedule</h2>
      <p>We become an academy on 1st April 2014 with The Harrowby BRIDGE Academy Trust.</p>
      <p>“Pupils’ achievement has improved very quickly this year.” – Edvisor</p>
    </section>

    <div class="class-photo class-photo--room" role="img" aria-label="Photo of pupils working in a bright classroom"></div>
    <div class="class-photo class-photo--board" role="img" aria-label="Photo of a teacher at the chalkboard with a pupil"></div>

    <div class="pupils-photo" role="img" aria-label="Photo of four pupils standing with school bags and books"></div>

    <section class="why-box">
      <h2>Why Choose Us?</h2>
      <p>“A very different school to the one at the previous inspection.” – Edvisor</p>
      <p>“Pupils make a strong start in the school.”</p>
    </section>

    <div class="web-links">
      <div>www.thornburyprimary.example</div>
      <div>www.harrowbybridge.example</div>
    </div>

    <div class="trust-name"><span class="mark"></span><span>Harrowby Bridge Academy Trust</span></div>
  </main>
</body>
</html>
```